Packaging design for an cardboard box / carton for modern Scandinavian cushion covers

The design should be made on a finished pattern for a cardboard box / carton. Ideally, the design can be directly on a packaging manufacturer. The box should measure 250 x 180 x 50 mm. Skanidnavian packaging design for modern cushion covers with classic patterns. The color design of the packaging should be kept simple and not too overloaded. 10 euros on a cushion cover.

Target Market(s)

End customer / retail

Requirements
Must have
• The logo (see appendix) should be included as well as a cut-out through which the customer can see the pattern of the product.
Nice to have
• Please attach the German texts (see appendix) to the draft.

```html
<!DOCTYPE html>
<html lang="de">
<head>
<meta charset="utf-8">
<title>Faltschachtel Kissenbezug – Stanzform</title>
<link rel="stylesheet" href="https://fonts.googleapis.com/css2?family=Open+Sans:wght@400;600;700&display=swap">
<style>
  :root {
    --brand-blue: #21a4c6;
    --die-line: #9a9a9a;
    --paper: #ffffff;
    --ink: #111111;
    --fabric-light: #d6efe9;
    --fabric-mid: #a9dcd3;
  }
  html, body {
    margin: 0;
    padding: 0;
    width: 976px;
    height: 1200px;
    overflow: hidden;
    background: var(--paper);
    font-family: "Open Sans", sans-serif;
  }
  .dieline-sheet {
    position: relative;
    width: 976px;
    height: 1200px;
  }
  .dieline-shapes {
    position: absolute;
    inset: 0;
    width: 976px;
    height: 1200px;
  }
  .cut-line {
    fill: var(--paper);
    stroke: var(--die-line);
    stroke-width: 1;
    vector-effect: non-scaling-stroke;
  }
  .side-band { fill: var(--brand-blue); }

  .band-url {
    position: absolute;
    left: 0;
    width: 976px;
    text-align: center;
    color: var(--paper);
    font-size: 21px;
    font-weight: 400;
    letter-spacing: 0.2px;
  }
  .band-url--top { top: 527px; }
  .band-url--bottom { top: 1071px; }

  /* Back panel, printed upside down */
  .back-copy {
    position: absolute;
    left: 282px;
    top: 161px;
    width: 434px;
    height: 250px;
    transform: rotate(180deg);
    color: var(--brand-blue);
  }
  .back-copy p {
    margin: 0 0 16px;
    font-size: 13px;
    line-height: 1.5;
    text-align: justify;
  }
  .back-wordmark {
    position: absolute;
    right: 0;
    bottom: 0;
    display: flex;
    align-items: center;
    gap: 6px;
    font-size: 13px;
    font-weight: 600;
    color: var(--brand-blue);
  }
  .back-wordmark .mark-dot {
    width: 18px;
    height: 18px;
    border-radius: 50%;
    background: var(--brand-blue);
  }

  /* Front panel */
  .front-headline {
    position: absolute;
    left: 264px;
    top: 694px;
    margin: 0;
    color: var(--brand-blue);
    font-size: 18px;
    font-weight: 700;
    line-height: 1.25;
  }
  .front-wordmark {
    position: absolute;
    left: 536px;
    top: 676px;
    display: flex;
    align-items: center;
    gap: 8px;
    font-size: 20px;
    font-weight: 700;
    color: var(--brand-blue);
    white-space: nowrap;
  }
  .front-wordmark .mark-dot {
    width: 42px;
    height: 42px;
    border-radius: 50%;
    background: var(--brand-blue);
  }
  .product-window {
    position: absolute;
    left: 267px;
    top: 794px;
    width: 228px;
    height: 164px;
    border-radius: 12px;
    background: radial-gradient(circle at 40% 50%, var(--fabric-light), var(--fabric-mid));
  }
  .product-facts {
    position: absolute;
    left: 553px;
    top: 850px;
    margin: 0;
    padding: 0;
    list-style: none;
    color: var(--ink);
    font-size: 16px;
    line-height: 1.4;
  }
  .product-facts li::before {
    content: "• ";
  }
</style>
</head>
<body>
<main class="dieline-sheet">
  <svg class="dieline-shapes" viewBox="0 0 720 880" preserveAspectRatio="none" aria-hidden="true">
    <polygon class="cut-line" points="60,58 147,45 147,358 60,340"/>
    <rect class="cut-line" x="147" y="45" width="431" height="313"/>
    <polygon class="cut-line" points="578,45 663,58 663,340 578,358"/>
    <polygon class="side-band" points="60,365 147,358 578,358 663,365 663,432 578,440 147,440 60,432"/>
    <polygon class="cut-line" points="60,455 147,443 147,755 60,740"/>
    <rect class="cut-line" x="147" y="443" width="431" height="312"/>
    <polygon class="cut-line" points="578,443 663,455 663,740 578,755"/>
    <polygon class="side-band" points="60,762 147,755 578,755 663,762 663,832 578,840 147,840 60,832"/>
  </svg>

  <section class="back-copy">
    <p>Mit diesem Kissenbezug erwerben Sie nicht nur einen Hingucker der Ihrem Sofa den letzten Hauch Gemütlichkeit und Stil verpasst, sondern entscheiden sich auch für 100% Qualität und Langlebigkeit.</p>
    <p>Unsere Kissenbezüge bestehen aus 100% Leinen bzw. Baumwolle und wurden von unseren sorgfältig ausgewählten Partnern nachhaltig hergestellt.</p>
    <div class="back-wordmark"><span class="mark-dot"></span>dein-sofaheim.de</div>
  </section>

  <div class="band-url band-url--top">dein-sofaheim.de</div>

  <h1 class="front-headline">Gemütlichkeit im<br>Skandinavischen Stil</h1>
  <div class="front-wordmark"><span class="mark-dot"></span>dein-sofaheim.de</div>
  <div class="product-window" role="img" aria-label="Sichtfenster mit Blick auf das mintfarbene Kissenbezugsmuster"></div>
  <ul class="product-facts">
    <li>45 x45 cm</li>
    <li>100 % Leinen</li>
    <li>Mit Reissverschluss</li>
  </ul>

  <div class="band-url band-url--bottom">dein-sofaheim.de</div>
</main>
</body>
</html>
```